Magician | Speaker looks for an innovative business card design

I'm a magician and public speaker offering artistic and modern magical experiences.
I'm based in Brussels (Belgium.) I love magic performed up-close, creating a space of intimacy, even when I'm on stage.
The final design should communicate professionalism, elegance, artistry, and a friendly kind personality

I would like to see designs based either on my photos and/or the way I sign my name Theo Varn (see attached files for more info.)
Additional photos and more info about what I offer can be seen at www.theo-varn.net

My current business card design is also attached. I like the fact that the reverse of my current design includes quotes from master magicians about magic, changing the way my participants see the art of magic.

Note: I would like a double-sided card design. However, I need white space on the reverse to be able to write things on for my performances.

Details to include on the card:
Artist name: Theo Varn
Offer: magician + (public) speaker or magic + (public) speaking (the + sign can be replaced by another character, like a bullet or a pipe)
Phone: +32 471 236 519
Email: book@theo-varn.net
(optional) Website: www.theo-varn.net or theo-varn.net

Target Market(s)

Corporate, organisations, companies as well as individuals

Industry/Entity Type

Artists

Colors

Designer to choose colors to be used in the design.

Requirements
Nice to have
• A side with a mirror could be nice

```html
<!DOCTYPE html>
<html lang="en">
<head>
<meta charset="utf-8">
<title>Theo Varn – Business Card</title>
<link href="https://fonts.googleapis.com/css2?family=Open+Sans:wght@400;500&display=swap" rel="stylesheet">
<style>
  :root {
    --navy: #27314f;
    --card: #ececec;
    --ink: #1c1f2a;
    --backdrop: #2b2b2b;
    --band-text: #d9dce4;
  }
  * { margin: 0; padding: 0; box-sizing: border-box; }
  html, body { width: 1200px; height: 600px; overflow: hidden; }
  body {
    background: var(--backdrop);
    font-family: "Open Sans", Arial, sans-serif;
    color: var(--ink);
    position: relative;
  }
  .card {
    position: absolute;
    top: 149px;
    width: 520px;
    height: 303px;
    background: var(--card);
    border-radius: 18px;
    overflow: hidden;
  }
  .card--front { left: 60px; }
  .card--back { left: 620px; }

  .name-bar {
    position: absolute;
    left: 24px; top: 21px;
    width: 9px; height: 47px;
    background: var(--navy);
  }
  .artist-name {
    position: absolute;
    left: 39px; top: 22px;
    font-size: 23px;
    font-weight: 400;
    line-height: 1;
    color: var(--ink);
  }
  .artist-role {
    position: absolute;
    left: 40px; top: 52px;
    font-size: 11.5px;
    font-weight: 500;
    color: var(--navy);
    letter-spacing: 0.1px;
    white-space: nowrap;
  }
  .portrait {
    position: absolute;
    background: linear-gradient(135deg, #2c3858 0%, var(--navy) 60%, #1f2842 100%);
  }
  .card--front .portrait { left: 372px; top: 18px; width: 125px; height: 117px; }
  .card--back .portrait { left: 178px; top: 64px; width: 160px; height: 150px; }

  .contact-list {
    position: absolute;
    left: 24px; top: 222px;
    list-style: none;
  }
  .contact-item {
    display: flex;
    align-items: center;
    gap: 5px;
    height: 25.5px;
    font-size: 14px;
    color: var(--ink);
    white-space: nowrap;
  }
  .contact-icon { width: 12px; height: 12px; fill: var(--ink); flex: none; }

  .role-band {
    position: absolute;
    left: 0; right: 0; bottom: 0;
    height: 60px;
    background: var(--navy);
    display: flex;
    align-items: center;
    justify-content: center;
    font-size: 12.5px;
    color: var(--band-text);
    letter-spacing: 0.2px;
  }
</style>
</head>
<body>
  <section class="card card--front" aria-label="Business card front">
    <div class="name-bar"></div>
    <h1 class="artist-name">Theo Varn</h1>
    <p class="artist-role">MAGICIAN + (PUBLIC) SPEAKER</p>
    <div class="portrait" role="img" aria-label="Portrait photo of Theo Varn with his signature"></div>
    <ul class="contact-list">
      <li class="contact-item">
        <svg class="contact-icon" viewBox="0 0 12 12" aria-hidden="true"><path d="M1 4.2C1 2.8 3 2 6 2s5 .8 5 2.2v1H8.4V4.3H3.6v.9H1z"/><rect x="2" y="6" width="8" height="4.5" rx="0.8"/></svg>
        <span>+32 471 236 519</span>
      </li>
      <li class="contact-item">
        <svg class="contact-icon" viewBox="0 0 12 12" aria-hidden="true"><path d="M0.5 2.5h11v7h-11z"/><path d="M0.8 2.8L6 6.8l5.2-4" fill="none" stroke="#ececec" stroke-width="1"/></svg>
        <span>book@theo-varn.net</span>
      </li>
      <li class="contact-item">
        <svg class="contact-icon" viewBox="0 0 12 12" aria-hidden="true" fill="none" stroke="#1c1f2a" stroke-width="0.9"><circle cx="6" cy="6" r="5"/><ellipse cx="6" cy="6" rx="2.2" ry="5"/><path d="M1 6h10M2 3.3h8M2 8.7h8"/></svg>
        <span>www.theo-varn.net or theo-varn.net</span>
      </li>
    </ul>
  </section>

  <section class="card card--back" aria-label="Business card back">
    <div class="portrait" role="img" aria-label="Portrait photo of Theo Varn with his signature"></div>
    <p class="role-band">MAGICIAN + (PUBLIC) SPEAKER</p>
  </section>
</body>
</html>
```